Spiritual Healing bussiness needs logo/business card

Simple, clean looking logo/card
For spiritual business with healing services and occult rituals

Contact Information for Business Card

Needs my name: Tovin Harlowe
Business name: Velka Healing Shop
Services provided and worded in this way:

Reiki Healing
Tarot
Oils
Rituals Of Change

Can look occult like but with light energy.

Colors
0255a3
3276b5
85abd2
33a6d7
85cae6
0292cd

```html
<!DOCTYPE html>
<html lang="en">
<head>
<meta charset="utf-8">
<title>Velka Healing Shop – Business Card</title>
<link href="https://fonts.googleapis.com/css2?family=Roboto+Slab:wght@400&family=Lato:wght@400&display=swap" rel="stylesheet">
<style>
  :root {
    --stage: #3d3d3d;
    --card-white: #ffffff;
    --deep-blue: #0255a3;
    --mid-blue: #3276b5;
    --sky-blue: #33a6d7;
    --bright-blue: #0292cd;
    --pale-blue: #85cae6;
    --ink: #2e2e2e;
    --rule-grey: #8a8a8a;
  }
  * { margin: 0; padding: 0; box-sizing: border-box; }
  html, body { width: 1200px; height: 900px; overflow: hidden; }
  body { background: var(--stage); position: relative; font-family: "Lato", sans-serif; }

  .card {
    position: absolute;
    width: 478px;
    height: 294px;
    box-shadow: 2px 3px 4px rgba(0,0,0,0.45);
  }
  .card-front {
    left: 120px; top: 275px;
    background: var(--card-white);
    border-radius: 0 52px 0 52px;
  }
  .card-back {
    left: 620px; top: 276px;
    border-radius: 52px 0 52px 0;
    background: radial-gradient(ellipse 300px 220px at 230px 110px, #0aa0db 0%, #0679c0 45%, var(--deep-blue) 100%);
    color: #fff;
  }

  /* front: brand mark area */
  .brand-block {
    position: absolute;
    left: 52px; top: 74px;
    width: 150px;
    display: flex; flex-direction: column; align-items: center; gap: 10px;
  }
  .brand-ring {
    width: 66px; height: 66px;
    border: 7px solid var(--deep-blue);
    border-radius: 50%;
  }
  .brand-name {
    font-family: "Roboto Slab", serif;
    font-size: 17px;
    line-height: 1.2;
    color: var(--deep-blue);
    text-align: center;
  }

  .divider {
    position: absolute;
    left: 219px; top: 98px;
    width: 1px; height: 97px;
    background: var(--rule-grey);
  }

  .person-name {
    position: absolute;
    left: 240px; top: 94px;
    font-family: "Roboto Slab", serif;
    font-size: 19px;
    color: var(--deep-blue);
    white-space: nowrap;
  }
  .person-name .surname { color: var(--bright-blue); }

  .contact-list {
    position: absolute;
    left: 239px; top: 140px;
    list-style: none;
  }
  .contact-list li {
    display: flex; align-items: center;
    height: 18px;
    font-size: 14px;
    color: var(--ink);
  }
  .contact-icon { width: 16px; height: 16px; margin-right: 3px; flex: none; }

  /* back */
  .back-ring {
    position: absolute;
    left: 172px; top: 54px;
    width: 112px; height: 112px;
    border: 9px solid #fff;
    border-radius: 50%;
  }
  .shop-name {
    position: absolute;
    left: 0; right: 0; top: 174px;
    text-align: center;
    font-family: "Roboto Slab", serif;
    font-size: 26px;
    letter-spacing: 0.3px;
    color: #fff;
  }
  .back-rule {
    position: absolute;
    left: 70px; top: 222px;
    width: 334px; height: 1px;
    background: var(--sky-blue);
  }
  .service-list {
    position: absolute;
    left: 0; right: 0; top: 237px;
    display: flex; justify-content: center; align-items: center;
    list-style: none;
    font-size: 14px;
    color: #e6f2fb;
  }
  .service-list li + li::before {
    content: "";
    display: inline-block;
    width: 6px; height: 6px;
    border-radius: 50%;
    background: #fff;
    margin: 0 12px 2px;
    vertical-align: middle;
  }
</style>
</head>
<body>

<section class="card card-front">
  <div class="brand-block">
    <div class="brand-ring"></div>
    <div class="brand-name">Velka Healing Shop</div>
  </div>
  <div class="divider"></div>
  <h1 class="person-name">Tovin <span class="surname">Harlowe</span></h1>
  <ul class="contact-list">
    <li>
      <svg class="contact-icon" viewBox="0 0 16 16" aria-hidden="true">
        <circle cx="8" cy="8" r="7" fill="none" stroke="#0255a3" stroke-width="1.3"/>
        <path d="M4.5 6.5h7v1.2l-1.6 0.6v2.9h-3.8v-2.9l-1.6-0.6z" fill="#0255a3"/>
      </svg>
      061-482 730 415
    </li>
    <li>
      <svg class="contact-icon" viewBox="0 0 16 16" aria-hidden="true">
        <circle cx="8" cy="8" r="7" fill="none" stroke="#0255a3" stroke-width="1.3"/>
        <rect x="4.3" y="5.3" width="7.4" height="5.4" fill="#0255a3"/>
        <path d="M4.5 5.6l3.5 2.8 3.5-2.8" fill="none" stroke="#fff" stroke-width="0.8"/>
      </svg>
      hello@velkamail.com
    </li>
    <li>
      <svg class="contact-icon" viewBox="0 0 16 16" aria-hidden="true">
        <circle cx="8" cy="8" r="7" fill="none" stroke="#0255a3" stroke-width="1.3"/>
        <circle cx="8" cy="8" r="4" fill="#0255a3"/>
      </svg>
      www.VelkaHealingShop.com
    </li>
  </ul>
</section>

<section class="card card-back">
  <div class="back-ring"></div>
  <h2 class="shop-name">Velka Healing Shop</h2>
  <div class="back-rule"></div>
  <ul class="service-list">
    <li>Reiki Healing</li>
    <li>Tarot</li>
    <li>Oils</li>
    <li>Rituals Of Change</li>
  </ul>
</section>

</body>
</html>
```